OLU58 biz card & Stationery

LU58 is a personalized shopping experience brought to you, that lets you find and discover fashion goods through a collection of boutiques curated by taste-makers - celebrities, stylists, designers, and fashion bloggers. Boutiques uses visual technology to help fashionistas discover and shop their look and creates the opportunity for designers to showcase their collections and latest inspirations online.

OLU58 is built on technology developed by our team of fashion experts who work with engineers to “teach” our computer systems to understand various patterns, pairings, and genre definitions. When signed into your account, OLU58 learns about your style and preferences and in turn, provides you better results and recommendations over time. Ultimately, OLU58 will provide shoppers with a much richer and interactive shopping experience and help drive traffic to retailers' websites.

We need a definitely cool business card. The card must be black! And must use our official logo which can be download from OLU58.com

The address for Letter head and evenlop, please use 4872 Crestwick Parkway, Sutie 510 Los Angeles CA90412, email will be anyone@OLU58.com, website is www.OLU58.com

thanks

We received some of the design, thanks. But most of the design are not what we want. We need a very clean version with black ground, you may also use some dark gray to add the element. please take a look at http://morvalstudio.no/work/#pelter__ostrama/, we do like this kind of design very much. hope it help.

```html
<!DOCTYPE html>
<html lang="en">
<head>
<meta charset="utf-8">
<title>OLU58 Business Card &amp; Stationery</title>
<link rel="stylesheet" href="https://fonts.googleapis.com/css2?family=Arimo:wght@400;700&family=Pinyon+Script&display=swap">
<style>
  :root {
    --ink: #000000;
    --paper: #ffffff;
    --backdrop: #dcebf6;
    --graphite: #2e2e2e;
    --steel: #8a8f94;
    --info-font: "Arimo", sans-serif;
    --script-font: "Pinyon Script", cursive;
  }
  * { box-sizing: border-box; margin: 0; padding: 0; }
  html, body { width: 1200px; height: 900px; overflow: hidden; }
  body { background: var(--backdrop); position: relative; font-family: var(--info-font); }

  .brand-name { font-family: var(--info-font); font-weight: 700; line-height: 1; color: var(--paper); }

  /* Letterhead */
  .letterhead {
    position: absolute; left: 38px; top: 37px; width: 414px; height: 527px;
    background: var(--ink); overflow: hidden;
  }
  .letterhead__strip {
    position: absolute; left: 0; top: 527px; width: 527px; height: 37px;
    transform: rotate(-90deg); transform-origin: 0 0;
    display: flex; align-items: center; gap: 40px; padding-left: 8px; white-space: nowrap;
  }
  .strip-name { font-family: var(--info-font); font-weight: 700; font-size: 22px; color: var(--graphite); }
  .letterhead__contact {
    position: absolute; left: 39px; top: 30px; color: var(--paper); font-style: normal;
    font-size: 7px; font-weight: 700; line-height: 12.5px; letter-spacing: 0.3px;
  }
  .letterhead__brand { position: absolute; right: 17px; top: 22px; }
  .letterhead__brand .brand-name { font-size: 36px; }
  .letterhead__rule { position: absolute; left: 37px; right: 0; top: 78px; height: 2px; background: var(--paper); }
  .letterhead__body {
    position: absolute; left: 40px; top: 85px; right: 0; bottom: 0;
    background: var(--paper); border-radius: 22px;
  }

  /* Envelope */
  .envelope {
    position: absolute; left: 572px; top: 177px; width: 568px; height: 270px;
    background: linear-gradient(to bottom, var(--ink) 0%, var(--ink) 22%, #3a3a3a 42%, #bdbdbd 62%, var(--paper) 76%);
    box-shadow: 0 1px 3px rgba(0,0,0,0.25);
  }
  .envelope__brand { position: absolute; right: 12px; top: 16px; }
  .envelope__brand .brand-name { font-size: 34px; }
  .envelope__window {
    position: absolute; left: 23px; top: 80px; width: 273px; height: 87px;
    border-radius: 9px; background: linear-gradient(to bottom, #d9d9d9, #f2f2f2);
    border: 1px solid #9a9a9a; box-shadow: inset 0 2px 4px rgba(0,0,0,0.25);
  }
  .envelope__contact {
    position: absolute; left: 0; right: 0; bottom: 6px; text-align: center;
    font-size: 9.5px; font-weight: 700; letter-spacing: 0.6px; color: var(--ink);
  }

  /* Business card */
  .biz-card {
    position: absolute; left: 720px; top: 617px; width: 418px; height: 247px;
    background: var(--ink); border: 2px solid var(--steel); border-radius: 3px; overflow: hidden;
  }
  .biz-card__brand {
    position: absolute; right: 18px; top: 18px; height: 210px;
    writing-mode: vertical-rl;
  }
  .biz-card__brand .brand-name { font-size: 56px; }
  .biz-card__holder { position: absolute; left: 0; width: 312px; top: 80px; text-align: center; color: var(--paper); }
  .holder-name { font-family: var(--script-font); font-size: 17px; }
  .holder-role { font-size: 11px; font-weight: 700; letter-spacing: 1.5px; margin-top: 1px; }
  .biz-card__contact {
    position: absolute; left: 15px; bottom: 14px; color: var(--paper); font-style: normal;
    font-size: 10px; line-height: 13px; letter-spacing: 1px;
  }
</style>
</head>
<body>

<section class="letterhead" aria-label="Letterhead">
  <div class="letterhead__strip" aria-hidden="true">
    <span class="strip-name">OLU58</span>
    <span class="strip-name">OLU58</span>
    <span class="strip-name">OLU58</span>
    <span class="strip-name">OLU58</span>
    <span class="strip-name">OLU58</span>
  </div>
  <address class="letterhead__contact">
    4872 Crestwick Parkway,<br>
    Sutie 510 Los Angeles CA90412<br>
    anyone@OLU58.com<br>
    www.OLU58.com
  </address>
  <div class="letterhead__brand"><div class="brand-name">OLU58</div></div>
  <div class="letterhead__rule"></div>
  <div class="letterhead__body"></div>
</section>

<section class="envelope" aria-label="Envelope">
  <div class="envelope__brand"><div class="brand-name">OLU58</div></div>
  <div class="envelope__window"></div>
  <p class="envelope__contact">4872 Crestwick Parkway, Sutie 510 Los Angeles CA90412 anyone@OLU58.com&nbsp;&nbsp; www.OLU58.com</p>
</section>

<section class="biz-card" aria-label="Business card">
  <div class="biz-card__brand"><div class="brand-name">OLU58</div></div>
  <div class="biz-card__holder">
    <div class="holder-name">Card Holder's Name Here</div>
    <div class="holder-role">Position</div>
  </div>
  <address class="biz-card__contact">
    4872 Crestwick Parkway,<br>
    Sutie 510 Los Angeles CA90412<br>
    anyone@OLU58.com<br>
    www.OLU58.com
  </address>
</section>

</body>
</html>
```